BRL Capital Campaign PWRPT Design

Our school is going to do a fund-raising campaign. I want to design a pwrpt around the campaign and need a design template using some of the images and the content I have laid out.

```html
<!DOCTYPE html>
<html lang="en">
<head>
<meta charset="utf-8">
<title>BRL Capital Campaign Slides</title>
<link href="https://fonts.googleapis.com/css2?family=Montserrat:ital,wght@0,400;0,500;0,600;0,700;0,800;1,600;1,800&display=swap" rel="stylesheet">
<style>
:root{
  --orange:#f97a4b;
  --amber:#ffa31a;
  --yellow:#ffc23a;
  --ink:#3a3a3a;
  --foot:#4b5355;
  --page:#ecebe8;
  --white:#ffffff;
}
*{box-sizing:border-box;margin:0;padding:0}
html,body{width:1200px;height:1200px;overflow:hidden;background:var(--page);font-family:"Montserrat",sans-serif;color:var(--ink)}
.canvas{position:relative;width:1200px;height:1200px}

/* title slide */
.hero{position:absolute;left:200px;top:25px;width:800px;height:450px;overflow:hidden;background:var(--white);box-shadow:0 4px 18px rgba(0,0,0,.12)}
.hero-photo{position:absolute;inset:0 0 22px 0;background:linear-gradient(180deg,#9fbf8a 0%,#6f9a5c 28%,#b9b3a6 55%,#d8cfc4 75%,#8c8a8e 100%)}
.hero-banner{position:absolute;left:0;bottom:80px;width:480px;height:118px;background:var(--orange);clip-path:polygon(0 0,92% 0,100% 100%,0 100%);padding:22px 0 0 26px;color:var(--white)}
.hero-banner::after{content:"";position:absolute;right:0;top:0;width:40px;height:100%;background:var(--yellow);clip-path:polygon(30% 0,40% 0,100% 100%,90% 100%)}
.hero-banner .kicker{font-weight:500;font-size:30px;letter-spacing:.02em}
.hero-banner .title{font-weight:700;font-size:36px;letter-spacing:.01em;margin-top:4px}
.hero-logo{position:absolute;right:0;bottom:100px;width:300px;height:90px;background:var(--white);clip-path:polygon(12% 0,100% 0,100% 100%,0 100%);display:flex;align-items:center;justify-content:flex-end;padding-right:26px}
.hero-foot{position:absolute;left:0;right:0;bottom:0;height:22px;background:var(--foot);color:#dfe3e3;font-size:9px;display:flex;align-items:center;padding-left:16px}

/* brand mark */
.brand{display:flex;align-items:center;gap:5px;font-weight:500;color:var(--ink)}
.brand .dot{width:9px;height:9px;background:var(--orange)}
.brand .name{font-size:14px}
.hero-logo .brand .dot{width:22px;height:22px}
.hero-logo .brand .name{font-size:40px}

/* grid */
.grid{position:absolute;left:5px;top:495px;display:grid;grid-template-columns:repeat(3,390px);grid-template-rows:repeat(3,220px);gap:10px}
.slide{position:relative;width:390px;height:220px;background:var(--white);overflow:hidden;box-shadow:0 2px 8px rgba(0,0,0,.08)}
.slide-head{position:absolute;top:0;left:0;right:0;height:38px;display:flex;align-items:center;justify-content:space-between;padding:4px 12px 0 14px}
.slide-head::before{content:"";position:absolute;top:6px;left:10px;width:180px;height:2px;background:var(--yellow)}
.slide-head h2{font-weight:800;font-size:12.5px;letter-spacing:.01em;color:var(--ink)}
.slide-head h2 .accent{color:var(--orange)}
.body{position:absolute;top:38px;left:0;right:0;bottom:9px}
.photo{position:absolute;top:0;bottom:0;left:40%;right:0}
.edge{position:absolute;inset:0;background:var(--yellow);clip-path:polygon(0 0,47.5% 0,56.5% 100%,0 100%)}
.panel{position:absolute;inset:0;background:var(--orange);clip-path:polygon(0 0,46% 0,55% 100%,0 100%);padding:8px 0 0 8px;color:var(--white)}
.panel.amber{background:var(--amber)}
.panel .lead{font-size:7.5px;font-weight:500;width:180px;line-height:1.35}
.panel .lead b{font-weight:700}
.panel .verse{font-size:5px;line-height:1.45;width:170px;margin-top:7px;text-align:justify}
.panel .ref{font-size:5px;margin-top:7px;line-height:1.5}
.panel .ref a{color:var(--yellow);text-decoration:none}
.panel ul{list-style:none;margin-top:4px;font-size:6px;line-height:1.6;font-weight:500}
.panel ul li::before{content:"";display:inline-block;width:0;height:0;border-left:3px solid transparent;border-right:3px solid transparent;border-bottom:5px solid var(--white);margin-right:4px}
.foot{position:absolute;left:0;right:0;bottom:0;height:9px;background:var(--foot);color:#d9dddd;font-size:4.5px;display:flex;align-items:center;padding-left:5px}

.panel .big{font-size:16px;line-height:1.3;font-weight:500;width:200px;margin-top:6px}
.panel .big b{font-weight:800}
.panel .mid{font-size:11.5px;line-height:1.3;font-weight:500;width:180px;margin-top:6px}
.panel .mid b{font-weight:800}

/* photo tones */
.ph-lab{background:linear-gradient(120deg,#3d4b57,#8ea0ad 45%,#e6c9b4 70%,#7b5a49)}
.ph-team{background:linear-gradient(120deg,#d9dde3,#f1f1f4 40%,#c9a98f 65%,#4a3e74)}
.ph-friends{background:linear-gradient(110deg,#5a4a3f,#e3c2a5 40%,#c7a184 65%,#3e3530)}
.ph-class{background:linear-gradient(180deg,#6d8fb5,#e6b2a6 45%,#6f7a60 55%,#b3a395)}
.ph-family{background:linear-gradient(110deg,#746d66,#cfb09a 45%,#6fc4d9 75%,#5a5650)}
.ph-computers{background:linear-gradient(110deg,#6e7f98,#e7d7c7 40%,#3b6aa8 70%,#2d3240)}
.ph-map{position:absolute;inset:0;background:linear-gradient(100deg,#7c8b6e,#4c8b3c 30%,#7fbf64 55%,#a39483 75%,#8a9180)}
.ph-group{position:absolute;inset:0;background:linear-gradient(180deg,#9fbf8a 0%,#6f9a5c 28%,#b9b3a6 55%,#d8cfc4 80%,#8c8a8e 100%)}

.tag{position:absolute;top:30px;left:0;background:var(--orange);color:var(--white);font-weight:700;font-size:7.5px;padding:4px 8px;letter-spacing:.02em}

/* phase 1 */
.school{position:absolute;left:0;top:0;bottom:0;width:36%;background:var(--orange);padding:34px 10px 0 10px;color:var(--white)}
.school .school-name{display:flex;align-items:center;gap:5px;font-weight:600;font-size:7.5px;letter-spacing:.08em}
.school .school-name .dot{width:12px;height:12px;border-radius:50%;background:var(--white)}
.school .addition{margin-top:38px;font-weight:700;font-size:9.5px;line-height:1.45}
.plan{position:absolute;left:36%;right:0;top:0;bottom:0;background:linear-gradient(135deg,#3f7d3a,#f3dc8f 30%,#8fe0b9 55%,#c9a2d9 70%,#f3dc8f 85%,#3f7d3a)}
.credits{position:absolute;left:38%;bottom:6px;display:flex;align-items:center;gap:12px;color:var(--white);font-size:6px}
.credits .firm{font-weight:700;font-size:9px;letter-spacing:.1em}
.credits .firm.small{font-size:7px;letter-spacing:.02em;font-weight:600}

/* closing slide */
.give{font-size:15.5px;line-height:1.3;width:170px;margin:22px 0 0 14px;font-style:italic;font-weight:600}
.give b{font-weight:800;font-size:17px}

/* title slide in grid */
.mini-banner{position:absolute;left:0;bottom:18px;width:225px;height:46px;background:var(--orange);clip-path:polygon(0 0,92% 0,100% 100%,0 100%);color:var(--white);padding:8px 0 0 12px}
.mini-banner .kicker{font-size:10px;font-weight:500}
.mini-banner .title{font-size:11.5px;font-weight:700;margin-top:1px}
.mini-logo{position:absolute;right:0;bottom:22px;width:140px;height:38px;background:var(--white);clip-path:polygon(14% 0,100% 0,100% 100%,0 100%);display:flex;justify-content:flex-end;align-items:center;padding-right:10px}
.mini-logo .brand .name{font-size:18px}
.mini-logo .brand .dot{width:12px;height:12px}
.mini-foot{position:absolute;left:0;right:0;bottom:0;height:9px;background:var(--foot);color:#d9dddd;font-size:4.5px;display:flex;align-items:center;padding-left:8px}
</style>
</head>
<body>
<main class="canvas">

  <section class="hero">
    <div class="hero-photo" role="img" aria-label="Photo of young students in hand-print t-shirts with their teacher outside the school"></div>
    <div class="hero-banner">
      <p class="kicker">PARTNER WITH US</p>
      <p class="title">PREPARE OUR FUTURE</p>
    </div>
    <div class="hero-logo"><div class="brand"><span class="dot"></span><span class="name">Pathwise</span></div></div>
    <div class="hero-foot">Pathwise Pathways 2018 Trademark Pathwise, LLC</div>
  </section>

  <section class="grid">

    <article class="slide">
      <header class="slide-head"><h2>ARE YOU IN <span class="accent">(DEBTED)</span></h2><div class="brand"><span class="dot"></span><span class="name">Pathwise</span></div></header>
      <div class="body">
        <div class="photo ph-lab" role="img" aria-label="Photo of a student smiling at a computer lab desk"></div>
        <div class="edge"></div>
        <div class="panel">
          <p class="lead"><b>Indebted</b> to the belief that we get to choose the culture for our children.</p>
          <p class="verse">“We are only servants through whom you believed. One planted the seed and another watered it, but God made it grow. The one who plants and the one who waters work together with the same purpose. You are God’s field, God’s building.”</p>
          <p class="ref">2 Corinthians 9:6-8 NLT<br><a>versebook.org/2co9.6-8</a></p>
        </div>
      </div>
      <footer class="foot">Copyright @Text</footer>
    </article>

    <article class="slide">
      <header class="slide-head"><h2>ARE YOU IN <span class="accent">(VESTED)</span></h2><div class="brand"><span class="dot"></span><span class="name">Pathwise</span></div></header>
      <div class="body">
        <div class="photo ph-team" role="img" aria-label="Photo of the basketball team celebrating in jerseys"></div>
        <div class="edge"></div>
        <div class="panel">
          <p class="lead"><b>invested</b> in the next generation</p>
          <ul><li>Invest in your child’s future</li><li>Invest in the next generation</li><li>Invest in our culture</li><li>Invest in the community</li></ul>
          <p class="verse">“Remember this: a farmer who plants only a few seeds will get a small crop, but the one who plants generously will get a generous crop. Give cheerfully, and you will always have plenty left over to share with others.”</p>
          <p class="ref">2 Corinthians 9:6-8 NLT<br><a>versebook.org/2co9.6-8</a></p>
        </div>
      </div>
      <footer class="foot">Copyright @Text</footer>
    </article>

    <article class="slide">
      <header class="slide-head"><h2>PHASE <span class="accent">2</span></h2><div class="brand"><span class="dot"></span><span class="name">Pathwise</span></div></header>
      <div class="body">
        <div class="ph-map" role="img" aria-label="Aerial master plan of the campus with sports fields and buildings"></div>
        <p class="tag">MASTER PLAN BUILDING</p>
      </div>
      <footer class="foot">Copyright @Text</footer>
    </article>

    <article class="slide">
      <header class="slide-head"><h2>ARE YOU IN <span class="accent">(FLUENTAIL)</span></h2><div class="brand"><span class="dot"></span><span class="name">Pathwise</span></div></header>
      <div class="body">
        <div class="photo ph-friends" role="img" aria-label="Photo of laughing teenage students"></div>
        <div class="edge"></div>
        <div class="panel">
          <p class="big"><b>influential</b> in your child’s future and the next generation.</p>
          <p class="verse">“By grace I have laid the foundation like an expert builder. Now others are building on it, and whoever builds must be very careful.”</p>
          <p class="ref">1 Corinthians 3:10 NLT<br><a>versebook.org/1co3.10</a></p>
        </div>
      </div>
      <footer class="foot">Copyright @Text</footer>
    </article>

    <article class="slide">
      <header class="slide-head"><h2>ARE YOU IN <span class="accent">(TUNE)</span></h2><div class="brand"><span class="dot"></span><span class="name">Pathwise</span></div></header>
      <div class="body">
        <div class="photo ph-class" role="img" aria-label="Photos of a young pupil on a colourful rug and older students working in class"></div>
        <div class="edge"></div>
        <div class="panel amber">
          <p class="mid"><b>in tune</b> with the cultural and learning aspects of your child’s future</p>
          <p class="verse">Do not conform to the pattern of <b>this world</b>, but be transformed by the renewing of your mind. Then you will be able to test and approve what God’s will is: good, pleasing and perfect.</p>
        </div>
      </div>
      <footer class="foot">Copyright @Text</footer>
    </article>

    <article class="slide">
      <header class="slide-head"><h2>ARE YOU IN <span class="accent">(VOLVED)</span></h2><div class="brand"><span class="dot"></span><span class="name">Pathwise</span></div></header>
      <div class="body">
        <div class="photo ph-family" role="img" aria-label="Photo of a mother and her teenage son by a stone fireplace"></div>
        <div class="edge"></div>
        <div class="panel">
          <p class="lead" style="font-size:8.5px"><b>involved</b> in the future of this community and lives of future children</p>
          <p class="verse">“Wake up and look around. The fields are already ripe for harvest. Joy awaits both the planter and the harvester alike. One plants and another harvests, and now you will get to gather the harvest.”</p>
          <p class="ref">John 4:35-38 NLT<br><a>versebook.org/jhn4.35-38</a></p>
        </div>
      </div>
      <footer class="foot">Copyright @Text</footer>
    </article>

    <article class="slide">
      <header class="slide-head"><h2>PHASE <span class="accent">1</span></h2><div class="brand"><span class="dot"></span><span class="name">Pathwise</span></div></header>
      <div class="body">
        <div class="school">
          <p class="school-name"><span class="dot"></span>BROOKRIDGE LEARNING</p>
          <p class="addition">BRL COURTYARD<br>BUILDING ADDITION</p>
        </div>
        <div class="plan" role="img" aria-label="Floor plan of new classrooms and science lab around a courtyard"></div>
        <div class="credits"><span>Architect By</span><span class="firm">HARBOR STUDIO</span><span class="firm small">Linden Design</span></div>
      </div>
      <footer class="foot"></footer>
    </article>

    <article class="slide">
      <div class="ph-group" role="img" aria-label="Photo of young students in hand-print t-shirts with their teacher outside the school"></div>
      <div class="mini-banner">
        <p class="kicker">PARTNER WITH US</p>
        <p class="title">PREPARE OUR FUTURE</p>
      </div>
      <div class="mini-logo"><div class="brand"><span class="dot"></span><span class="name">Pathwise</span></div></div>
      <div class="mini-foot">Pathwise Pathways 2018 Trademark Pathwise, LLC</div>
    </article>

    <article class="slide">
      <header class="slide-head"><h2>ARE YOU IN <span class="accent">(CLUDED)</span></h2><div class="brand"><span class="dot"></span><span class="name">Pathwise</span></div></header>
      <div class="body">
        <div class="photo ph-computers" role="img" aria-label="Photo of a teacher helping students in the computer lab"></div>
        <div class="edge"></div>
        <div class="panel amber">
          <p class="give"><b>Give today,</b> make a difference for tomorrow.</p>
        </div>
      </div>
      <footer class="foot">Copyright @Text</footer>
    </article>

  </section>
</main>
</body>
</html>
```